Larkwell Pharmacy opening

We want to have a double sided 5.5"x8.5" flyer for a new Pharmacy opening in a well known strip mall in the neighborhood and we are planning to mail it to neighbors homes.

Want to put the outside pharmacy picture on the main side of the flyer and a coupon with 25% off towards an OTC product on the back in addition to the info below (preferably in a sort of bulletin points not a list (something like the 2 examples attached).

Colors to be red like the exterior sign and blue like the interior wall paint:

Front side should have:
Larkwell pharmacy
Your locally owned and operated pharmacy around the corner.
317-4821 Pendry rd.
Ashcombe ridge plaza
T. 604 927 5583 (call or text)
F. 604-927-5587

Free prescription delivery
Text us for refills
Specialized compounding
Customized compression stockings

The back side should have:

Do you forget taking your medications! We offer multiple compliance packaging options at no additional cost.
Had shingles before or worried to have it? travelling soon? check our vaccinations options!
Suffering side effects? We are experienced to check your medications interactions & different coverage options.
Hard time monitoring your blood pressure? Trying to stop smoking? we can always help.

FEELING BETTER STARTS HERE

```html
<!DOCTYPE html>
<html lang="en">
<head>
<meta charset="utf-8">
<title>Larkwell Pharmacy – Opening Postcard</title>
<link rel="stylesheet" href="https://fonts.googleapis.com/css2?family=Open+Sans:wght@400;600;700;800&family=Arimo:wght@700&display=swap">
<style>
  :root {
    --red: #e31e24;
    --red-dark: #c4161c;
    --navy: #2d3d5e;
    --navy-deep: #1f2c47;
    --navy-soft: #3d5078;
    --white: #ffffff;
    --ink: #2a2f3a;
    --rule: #c9ccd2;
    --backdrop: #5b5b5b;
  }
  * { box-sizing: border-box; margin: 0; padding: 0; }
  html, body { width: 966px; height: 1200px; overflow: hidden; }
  body {
    background: var(--backdrop);
    font-family: "Open Sans", Arial, sans-serif;
    position: relative;
  }
  .postcard {
    position: absolute;
    left: 106px;
    width: 757px;
    height: 488px;
    background: var(--white);
    overflow: hidden;
    box-shadow: 6px 8px 14px rgba(0,0,0,.45);
  }
  .postcard--front { top: 86px; }
  .postcard--back { top: 630px; }
  .shapes { position: absolute; inset: 0; width: 757px; height: 488px; }

  .brand { position: absolute; left: 27px; top: 26px; display: flex; align-items: center; gap: 14px; }
  .brand__dot { width: 105px; height: 105px; border-radius: 50%; background: var(--red); flex: none; }
  .brand__dot--small { width: 80px; height: 80px; }
  .brand__name {
    font-family: "Arimo", Arial, sans-serif;
    font-weight: 700; font-size: 25px; line-height: 28px;
    color: var(--red); text-transform: uppercase; letter-spacing: .5px;
  }

  .tagline {
    position: absolute; left: 27px; top: 145px; width: 330px;
    font-size: 19px; line-height: 25px; font-weight: 600; color: var(--navy);
  }
  .now-open {
    position: absolute; left: 0; top: 220px; height: 50px; width: 310px;
    background: var(--red); color: var(--white);
    font-family: "Arimo", Arial, sans-serif; font-weight: 700; font-size: 37px;
    line-height: 50px; padding-left: 30px; letter-spacing: 1px;
    clip-path: polygon(0 0, 100% 0, 94% 100%, 0 100%);
  }
  .services { position: absolute; left: 25px; top: 290px; list-style: none; }
  .services li {
    display: flex; align-items: center; gap: 10px; height: 36px;
    color: var(--white); font-weight: 600; font-size: 17.5px;
  }
  .services .icon { width: 30px; height: 30px; border-radius: 50%; background: var(--red); border: 2px solid var(--white); flex: none; }

  .contact-bar {
    position: absolute; left: 0; bottom: 0; height: 47px; width: 470px;
    background: var(--red); color: var(--white);
    font-family: "Arimo", Arial, sans-serif; font-weight: 700; font-size: 18px;
    display: flex; align-items: center; gap: 10px; padding-left: 25px;
    clip-path: polygon(0 0, 97% 0, 100% 100%, 0 100%);
  }
  .contact-bar svg { flex: none; }
  .location-line {
    position: absolute; left: 480px; bottom: 13px;
    font-size: 13px; font-weight: 700; color: var(--navy);
  }
  .offer-badge {
    position: absolute; left: 425px; top: 341px; width: 106px; height: 106px;
    border-radius: 50%; background: var(--red); color: var(--white);
    text-align: center; padding-top: 27px; border: 3px solid var(--white);
  }
  .offer-badge__value { font-family: "Arimo", Arial, sans-serif; font-size: 19px; font-weight: 700; line-height: 22px; }
  .offer-badge__note { font-size: 10px; font-weight: 700; line-height: 12px; }

  /* back side */
  .callouts { position: absolute; left: 18px; top: 117px; width: 345px; }
  .callout { position: relative; height: 71px; }
  .callout__label {
    position: absolute; left: 0; top: 0; height: 24px;
    background: var(--red); color: var(--white); font-size: 11px; font-weight: 700;
    line-height: 24px; padding: 0 26px 0 18px; white-space: nowrap;
    clip-path: polygon(0 0, calc(100% - 12px) 0, 100% 100%, 0 100%);
    z-index: 2;
  }
  .callout__body {
    position: absolute; left: 0; top: 10px; height: 54px; width: 345px;
    background: var(--white); border-radius: 0 10px 10px 0;
    padding: 20px 62px 0 18px; font-size: 10.5px; line-height: 14px; color: var(--navy);
  }
  .callout__icon { position: absolute; right: 12px; top: 20px; }
  .slogan {
    position: absolute; left: 28px; top: 410px;
    color: var(--white); font-weight: 700; font-size: 17.5px;
  }
  .contact-bar--back { width: 368px; font-size: 19px; }

  .mailing { position: absolute; left: 427px; top: 36px; color: var(--ink); font-size: 16px; line-height: 21px; font-style: normal; }
  .mailing__name { color: var(--red); font-weight: 700; }
  .stamp-box { position: absolute; left: 632px; top: 30px; width: 99px; height: 74px; border: 1px solid var(--rule); }
  .address-rule { position: absolute; left: 463px; width: 268px; height: 1px; background: var(--rule); }
  .address-rule--1 { top: 184px; }
  .address-rule--2 { top: 228px; }
  .address-rule--3 { top: 274px; }
  .address-rule--4 { top: 320px; }
</style>
</head>
<body>

<section class="postcard postcard--front">
  <svg class="shapes" viewBox="0 0 757 488">
    <defs>
      <linearGradient id="panelFront" x1="0" y1="0" x2="1" y2="1">
        <stop offset="0" stop-color="#3a4d73"/>
        <stop offset="1" stop-color="#1f2c47"/>
      </linearGradient>
      <linearGradient id="storefront" x1="0" y1="0" x2="0" y2="1">
        <stop offset="0" stop-color="#b9bfc6"/>
        <stop offset=".45" stop-color="#d8d2c8"/>
        <stop offset="1" stop-color="#9aa3ad"/>
      </linearGradient>
      <linearGradient id="interior" x1="0" y1="0" x2="0" y2="1">
        <stop offset="0" stop-color="#3f5a8c"/>
        <stop offset="1" stop-color="#d9cfc0"/>
      </linearGradient>
    </defs>
    <polygon points="0,240 420,240 360,441 0,441" fill="url(#panelFront)"/>
    <path d="M400 0 H757 V441 H352 C335 300 345 120 400 0 Z" fill="var(--navy)"/>
    <path d="M420 0 C368 120 362 300 378 441" fill="none" stroke="var(--red)" stroke-width="5"/>
    <g role="img" aria-label="Photo of the pharmacy storefront with a pharmacist helping a customer">
      <path d="M440 0 H757 V441 H392 C380 300 390 120 440 0 Z" fill="url(#storefront)"/>
    </g>
    <circle cx="406" cy="331" r="76" fill="var(--white)"/>
    <g role="img" aria-label="Photo of the pharmacy interior with blue walls and product shelves">
      <circle cx="406" cy="331" r="70" fill="url(#interior)"/>
    </g>
  </svg>

  <div class="brand">
    <span class="brand__dot"></span>
    <span class="brand__name">Larkwell<br>Pharmacy</span>
  </div>

  <p class="tagline">Your locally owned and operated pharmacy around the corner.</p>
  <h1 class="now-open">NOW OPEN</h1>

  <ul class="services">
    <li><span class="icon"></span>Free prescription delivery</li>
    <li><span class="icon"></span>Text us for refills</li>
    <li><span class="icon"></span>Specialized compounding</li>
    <li><span class="icon"></span>Customized compression stockings</li>
  </ul>

  <div class="offer-badge">
    <div class="offer-badge__value">25% OFF</div>
    <div class="offer-badge__note">towards an<br>OTC product</div>
  </div>

  <div class="contact-bar">
    <span>CALL OR TEXT</span>
    <svg width="16" height="24" viewBox="0 0 16 24"><rect x="1" y="1" width="14" height="22" rx="3" fill="none" stroke="#fff" stroke-width="2"/><circle cx="8" cy="19" r="1.5" fill="#fff"/></svg>
    <span>604 927 5583&nbsp; F. 604-927-5587</span>
  </div>
  <p class="location-line">317-4821 Pendry rd. Ashcombe ridge plaza</p>
</section>

<section class="postcard postcard--back">
  <svg class="shapes" viewBox="0 0 757 488">
    <defs>
      <linearGradient id="panelBack" x1="0" y1="0" x2="1" y2="1">
        <stop offset="0" stop-color="#3a4d73"/>
        <stop offset="1" stop-color="#1f2c47"/>
      </linearGradient>
    </defs>
    <path d="M0 100 H290 C370 150 400 250 400 330 C400 400 390 445 380 488 H0 Z" fill="url(#panelBack)"/>
    <path d="M285 0 C395 70 430 210 422 330 C418 400 405 450 395 488" fill="none" stroke="var(--red)" stroke-width="5"/>
    <path d="M265 0 C370 60 410 200 405 320" fill="none" stroke="var(--navy)" stroke-width="8"/>
    <g role="img" aria-label="Photo of a smiling pharmacist in a white coat">
      <rect x="372" y="259" width="90" height="229" rx="6" fill="#dfe3e8"/>
    </g>
  </svg>

  <div class="brand">
    <span class="brand__dot brand__dot--small"></span>
    <span class="brand__name">Larkwell<br>Pharmacy</span>
  </div>

  <div class="callouts">
    <div class="callout">
      <div class="callout__label">Do you forget taking your medications!</div>
      <div class="callout__body">We offer multiple compliance packaging options at no additional cost.</div>
      <svg class="callout__icon" width="36" height="26" viewBox="0 0 36 26"><rect x="2" y="6" width="24" height="12" rx="6" fill="none" stroke="var(--navy)" stroke-width="2.5" transform="rotate(-20 14 12)"/><circle cx="28" cy="16" r="7" fill="none" stroke="var(--navy)" stroke-width="2.5"/></svg>
    </div>
    <div class="callout">
      <div class="callout__label">Had shingles before or worried to have it?</div>
      <div class="callout__body">Travelling soon? Check our vaccinations options!</div>
      <svg class="callout__icon" width="24" height="32" viewBox="0 0 24 32" style="top:16px"><rect x="3" y="7" width="18" height="22" rx="3" fill="var(--navy)"/><rect x="8" y="2" width="8" height="6" rx="1" fill="none" stroke="var(--navy)" stroke-width="2"/></svg>
    </div>
    <div class="callout">
      <div class="callout__label">Suffering side effects?</div>
      <div class="callout__body">We are experienced to check your medications interactions &amp; different coverage options.</div>
      <svg class="callout__icon" width="32" height="32" viewBox="0 0 32 32" style="top:16px"><rect x="3" y="3" width="20" height="25" rx="2" fill="none" stroke="var(--navy)" stroke-width="2"/><path d="M7 10h12M7 15h12M7 20h8" stroke="var(--navy)" stroke-width="2"/><circle cx="25" cy="25" r="6" fill="var(--navy)"/><path d="M22 25l2 2 4-4" stroke="#fff" stroke-width="1.8" fill="none"/></svg>
    </div>
    <div class="callout">
      <div class="callout__label">Hard time monitoring your blood pressure?</div>
      <div class="callout__body">Trying to stop smoking? We can always help.</div>
      <svg class="callout__icon" width="28" height="32" viewBox="0 0 28 32" style="top:16px"><path d="M4 2v10a8 8 0 0 0 16 0V2" fill="none" stroke="var(--navy)" stroke-width="2.5"/><path d="M12 20v4a6 6 0 0 0 12 0v-4" fill="none" stroke="var(--navy)" stroke-width="2.5"/><circle cx="24" cy="17" r="3" fill="none" stroke="var(--navy)" stroke-width="2"/></svg>
    </div>
  </div>

  <p class="slogan">FEELING BETTER STARTS HERE</p>

  <div class="contact-bar contact-bar--back">
    <span>CALL OR TEXT</span>
    <svg width="16" height="24" viewBox="0 0 16 24"><rect x="1" y="1" width="14" height="22" rx="3" fill="none" stroke="#fff" stroke-width="2"/><circle cx="8" cy="19" r="1.5" fill="#fff"/></svg>
    <span>604 927 5583</span>
  </div>

  <address class="mailing">
    <div class="mailing__name">Larkwell pharmacy</div>
    <div>317-4821 Pendry rd.</div>
    <div>Ashcombe ridge plaza</div>
  </address>
  <div class="stamp-box"></div>
  <div class="address-rule address-rule--1"></div>
  <div class="address-rule address-rule--2"></div>
  <div class="address-rule address-rule--3"></div>
  <div class="address-rule address-rule--4"></div>
</section>

</body>
</html>
```